Existing company needs Rebranding on logo and website!!

the company is called Harvest Bridge (www.harvestbridgefund.co.uk) check the site to see the existing site and logo, this has to change and must be completely different.

I want to the turn the website into a crowd funding site, but i want an inovative and interacive site. Have a look http://www.lendora.org/about/how or https://www.fundlarkly.com/ to get an idea of what is required. However i do not want my site to be anything like this. It is 2015 so web browser can do alot. when it comes to selecting project proposals on the site i want them them to pop up use your imagination your the desgner. ofcourse the site will be taking card payments and possibly bank transfers and maybe zentopay. the usual API are already on the site so you wont need to do much. the site is hosted by wordpress so i do prefer it to stay there. i am familiar with that platform.

interms of creativity you have full control we wil be working closely and i expect to be kept in the loop as things develope.

the site will also need to be turn into a mobile app which serves different purposes depending if your an investor or project sponsor.

i will give you all the information required we can communicate on chatvolt email or telephone i am flexible.

many thanks

Target Market(s)

Investors

Industry/Entity Type

Finance

Number of Pages Required

5+ page

Font styles to use
Sans Serif

Colors
3176b5
f04a50
abd036
00a990

Requirements
Must have
• i want the designer to look at my existing site www.harvestbridgefund.co.uk and come up with a better design concept.

```html
<!DOCTYPE html>
<html lang="en">
<head>
<meta charset="utf-8">
<title>Harvest Bridge – Crowdfunding</title>
<link href="https://fonts.googleapis.com/css2?family=Open+Sans:wght@400;600;700&display=swap" rel="stylesheet">
<style>
:root{
  --blue:#3176b5;
  --bar-blue:#2a90d4;
  --red:#f04a50;
  --green:#abd036;
  --teal:#00a990;
  --ink:#222;
  --muted:#777;
  --section-grey:#ebebed;
  --track:#d9d9d9;
  --footer:#000;
}
*{box-sizing:border-box;margin:0;padding:0}
html,body{width:814px;height:1200px;overflow:hidden}
body{position:relative;font-family:"Open Sans",Arial,sans-serif;color:var(--ink);background:#fff}
.abs{position:absolute}

/* top bar */
.topbar{left:0;top:0;width:814px;height:55px;background:var(--blue)}
.contact{top:16px;text-align:right;line-height:1.2;color:#fff;white-space:nowrap}
.contact small{display:block;font-size:8px}
.contact b{font-weight:400}
.call{right:257px}
.call b{font-size:11px}
.mail{right:111px;top:19px}
.mail b{font-size:8.5px}
.icon-phone{left:561px;top:18px}
.icon-mail{left:711px;top:26px}

/* header */
.header{left:0;top:55px;width:814px;height:58px;background:#fff}
.logo-tab{left:76px;top:35px;width:68px;height:68px;border-radius:50%;background:#fff}
.brand{display:flex;align-items:center;gap:7px;white-space:nowrap}
.brand .dot{width:28px;height:28px;border-radius:50%;background:var(--red)}
.brand span{font-weight:700;font-size:16px;color:var(--ink);line-height:1}
.brand-head{left:92px;top:70px}
.nav{left:279px;top:78px;display:flex;font-size:10px;white-space:nowrap}
.nav a{color:var(--ink);text-decoration:none;margin-right:20px}
.nav a:last-child{margin-right:0}
.nav a.active{color:var(--red)}

/* hero */
.hero{left:0;top:113px;width:814px;height:371px;
  background:linear-gradient(180deg,#2f8fd8 0%,#7fc0ee 35%,#d7ecf7 55%,#3fb7c6 68%,#1f9fae 80%,#e8d8b8 100%)}
.hero-badge{left:438px;top:214px;width:240px;height:240px;border-radius:50%;background:rgba(255,255,255,.62)}
.brand-hero{left:505px;top:262px}
.brand-hero .dot{width:26px;height:26px}
.brand-hero span{font-size:16px}
.hero-rule{left:505px;top:306px;width:140px;height:1px;background:rgba(0,0,0,.1)}
.hero-list{left:494px;top:324px;list-style:none;font-size:10.5px;color:#222}
.hero-list li{display:flex;align-items:center;height:21px}
.hero-list li i{width:11px;height:11px;border-radius:50%;border:2.5px solid var(--red);margin-right:13px}
.dots{left:390px;top:462px;display:flex;gap:3px}
.dots i{width:8px;height:8px;border-radius:50%;background:#fff}
.dots i.on{background:var(--red)}

/* staff picks */
.picks{left:0;top:484px;width:814px;height:269px;background:var(--section-grey)}
.section-title{font-size:11.5px;font-weight:600}
.picks-title{left:58px;top:509px}
.latest-title{left:58px;top:778px}
.feature-photo{left:58px;top:547px;width:198px;height:150px;background:linear-gradient(135deg,#333 0%,#4a4a4a 55%,#c9302c 100%)}
.feature{left:272px;top:544px;width:280px}
.feature h3{font-weight:400;font-size:11px}
.meta{display:flex;align-items:center;font-size:9px;color:var(--blue);margin-top:8px}
.meta span{display:flex;align-items:center;gap:6px}
.meta .sep{width:1px;height:11px;background:#ccc;margin:0 11px}
.meta i{width:8px;height:8px;border-radius:50%;background:var(--blue)}
.feature p{font-size:8px;line-height:15.5px;color:#555;margin-top:10px;width:276px}
.progress{height:10px;background:var(--track);position:relative}
.progress::after{content:"";position:absolute;left:0;top:0;bottom:0;width:var(--fill);background:var(--bar-blue)}
.feature .progress{width:227px;margin:10px 0 0 2px}
.stats{display:flex}
.stats div{border-left:1px solid #ccc;line-height:1.05}
.stats div:first-child{border-left:0;padding-left:0}
.stats b{display:block;font-weight:600}
.stats small{color:var(--muted)}
.feature .stats{margin:12px 0 0 3px}
.feature .stats div{padding:0 12px;font-size:9px}
.feature .stats div:first-child{padding-left:0}
.feature .stats b{font-size:15px}
.feature .stats small{font-size:9px}
.see-all{left:498px;top:719px;font-size:8.5px;color:var(--red)}

.cats{left:583px;top:537px;width:157px;height:175px;background:#f1f1f2;border:1px solid #e2e2e4}
.cats header{height:27px;background:var(--bar-blue);color:#fff;display:flex;align-items:center;padding-left:10px;font-size:10.5px;font-weight:600;gap:10px}
.cats header i{width:14px;height:14px;border-radius:50%;background:var(--red);border:2px solid #fff}
.cats ul{list-style:none;padding:9px 0 0 16px;font-size:8px}
.cats li{display:flex;align-items:center;height:18.5px}
.cats li i{width:7px;height:7px;border-radius:50%;background:var(--bar-blue);margin-right:9px}

/* latest projects */
.card{top:815px;width:193px;height:237px;background:#fff;border:1px solid #e6e6e6}
.card .photo{height:115px}
.card-a .photo{background:linear-gradient(180deg,#cfe0d9 0%,#9fae82 55%,#6f7064 100%)}
.card-b .photo{background:linear-gradient(180deg,#c5d7e8 0%,#a8a295 45%,#c0572c 75%,#9c5335 100%)}
.card-c .photo{background:linear-gradient(180deg,#dbe6ef 0%,#6b7d4c 50%,#5a5450 100%)}
.card h4{font-weight:400;font-size:9.5px;margin:9px 0 0 8px}
.card p{font-size:7px;line-height:12.5px;color:#666;margin:7px 0 0 8px;width:178px}
.card .progress{width:168px;height:7px;margin:10px 0 0 8px}
.card .stats{margin:10px 0 0 8px}
.card .stats div{padding:0 8px;font-size:6px}
.card .stats div:first-child{padding-left:0}
.card .stats b{font-size:9.5px}
.card .stats small{font-size:6px}
.card-a{left:59px}.card-b{left:288px}.card-c{left:516px}

/* footer */
.footer{left:0;top:1083px;width:814px;height:117px;background:var(--footer);color:#bbb}
.social{left:366px;top:1105px;display:flex;gap:3px}
.social i{width:18px;height:18px;border-radius:50%}
.footer-nav{left:0;top:1131px;width:814px;text-align:center;font-size:8.5px;color:#bbb}
.footer-nav a{color:#bbb;text-decoration:none}
.footer-nav em{font-style:normal;margin:0 12px}
.copy{left:0;top:1155px;width:814px;text-align:center;font-size:8.5px;color:#999}
</style>
</head>
<body>

<div class="abs topbar"></div>
<div class="abs contact call"><small>Call us</small><b>0161 555 0142</b></div>
<svg class="abs icon-phone" width="20" height="20" viewBox="0 0 20 20" aria-hidden="true"><circle cx="10" cy="10" r="8.5" fill="none" stroke="#fff" stroke-width="1.4"/><path d="M7 6c1 0 1.4 1.6 1 2.2-.4.5.4 1.8 1.6 2.8 1 .6 1.5.5 1.9.1.5-.4 2 .3 2 1.2-.2 1-1.3 1.6-2.3 1.3C8.8 13 6.3 10.3 6 8.1 5.9 7 6.3 6 7 6z" fill="#fff"/></svg>
<div class="abs contact mail"><small>Mail us</small><b>info@harvestbridge.com</b></div>
<svg class="abs icon-mail" width="16" height="12" viewBox="0 0 16 12" aria-hidden="true"><rect width="16" height="12" rx="1" fill="#fff"/><path d="M1 1.5l7 5 7-5" fill="none" stroke="#3176b5" stroke-width="1.4"/></svg>

<div class="abs header"></div>
<div class="abs logo-tab"></div>
<div class="abs brand brand-head"><i class="dot"></i><span>Harvest Bridge</span></div>
<nav class="abs nav">
  <a class="active" href="#">Home</a><a href="#">About Us</a><a href="#">About Ghana</a><a href="#">Why Ghana</a><a href="#">Sponsorship</a><a href="#">News &amp; Media</a><a href="#">Contact Us</a>
</nav>

<section class="abs hero" role="img" aria-label="Photo of a palm tree leaning over a tropical beach with turquoise sea and blue sky"></section>
<div class="abs hero-badge"></div>
<div class="abs brand brand-hero"><i class="dot"></i><span>Harvest Bridge</span></div>
<div class="abs hero-rule"></div>
<ul class="abs hero-list">
  <li><i></i>Developing Infrastructure</li>
  <li><i></i>Thriving Tourism</li>
  <li><i></i>Business and Marketing</li>
  <li><i></i>Natural Resources</li>
</ul>
<div class="abs dots"><i></i><i class="on"></i><i></i></div>

<section class="abs picks"></section>
<h2 class="abs section-title picks-title">Staff Picks :</h2>
<div class="abs feature-photo" role="img" aria-label="Photo of a speaker at a podium addressing an audience"></div>
<article class="abs feature">
  <h3>Ghana has the core elements forinvestment</h3>
  <div class="meta"><span><i></i>By Admin</span><em class="sep"></em><span><i></i>Mensah</span></div>
  <p>Vice President Mensah-Adjei said there are a lot of opportunities in the manufacturing and the energy sectors adding that the National Investment Office, the Free Zones Authority and other</p>
  <div class="progress" style="--fill:204px"></div>
  <div class="stats">
    <div><b>60%</b><small>Funded</small></div>
    <div><b>$9,525</b><small>pledged</small></div>
    <div><b>166</b><small>backers</small></div>
    <div><b>3</b><small>days to go</small></div>
  </div>
</article>
<a class="abs see-all">See All &gt;&gt;</a>

<aside class="abs cats">
  <header><i></i>Art</header>
  <ul>
    <li><i></i>Comics</li><li><i></i>Design</li><li><i></i>Flim &amp; Video</li><li><i></i>Games</li><li><i></i>Music</li><li><i></i>Photography</li><li><i></i>Technology</li>
  </ul>
</aside>

<h2 class="abs section-title latest-title">Latest Projects :</h2>

<article class="abs card card-a">
  <div class="photo" role="img" aria-label="Photo of a steel arch bridge over a tree-lined road"></div>
  <h4>RFS Goes High-Tech</h4>
  <p>Regional Fire Service (RFS), in collabora-tion with Nexa Systems Limited, has intro-duced a new technology escalates.</p>
  <div class="progress" style="--fill:121px"></div>
  <div class="stats"><div><b>60%</b><small>Funded</small></div><div><b>$9,525</b><small>pledged</small></div><div><b>166</b><small>backers</small></div><div><b>3</b><small>Days to go</small></div></div>
</article>
<article class="abs card card-b">
  <div class="photo" role="img" aria-label="Photo of a coastal castle above red rocks and surf"></div>
  <h4>RFS Goes High-Tech</h4>
  <p>Regional Fire Service (RFS), in collabora-tion with Nexa Systems Limited, has intro-duced a new technology escalates.</p>
  <div class="progress" style="--fill:121px"></div>
  <div class="stats"><div><b>60%</b><small>Funded</small></div><div><b>$9,525</b><small>pledged</small></div><div><b>166</b><small>backers</small></div><div><b>3</b><small>Days to go</small></div></div>
</article>
<article class="abs card card-c">
  <div class="photo" role="img" aria-label="Photo of a town street lined with palm trees and buildings"></div>
  <h4>RFS Goes High-Tech</h4>
  <p>Regional Fire Service (RFS), in collabora-tion with Nexa Systems Limited, has intro-duced a new technology escalates.</p>
  <div class="progress" style="--fill:121px"></div>
  <div class="stats"><div><b>60%</b><small>Funded</small></div><div><b>$9,525</b><small>pledged</small></div><div><b>166</b><small>backers</small></div><div><b>3</b><small>Days to go</small></div></div>
</article>

<footer class="abs footer"></footer>
<div class="abs social"><i style="background:#2aa9e0"></i><i style="background:#3b5998"></i><i style="background:#dd4b39"></i><i style="background:#0e76a8"></i></div>
<nav class="abs footer-nav">
  <a href="#">Home</a><em>|</em><a href="#">About us</a><em>|</em><a href="#">Why Ghana</a><em>|</em><a href="#">Sponsorship</a><em>|</em><a href="#">News &amp; Media</a><em>|</em><a href="#">Contact us</a>
</nav>
<p class="abs copy">© Copyright 2015 - Harvestbridge , All Rights Reserved.</p>

</body>
</html>
```